Business Card Design Project

We need a Business Card for an Mechanical Engineering firm in Singapore. The design should be Modern & Technical looking, yet eye catching.

Our company deals in Cutting Tools & Machine Accessories for the Manufacturing Industries such as Oil & Gas, Aero Space, etc... For more information on our Company, you can either email me or view our website www.valtrion.com.sg.

We are trying to revamp our image to give our consumers a fresh new perspective to our company, so we welcome all ideas.

Industry/Entity Type

Business

Requirements
Must have
• Must incorporate New Company Logo into the card as shown in Uploaded file.

```html
<!DOCTYPE html>
<html lang="en">
<head>
<meta charset="utf-8">
<title>Valtrion Tools – Business Card</title>
<link rel="stylesheet" href="https://fonts.googleapis.com/css2?family=Didact+Gothic&family=Open+Sans:wght@400&display=swap">
<style>
  :root {
    --crimson: #7a0030;
    --ink: #4a4e55;
    --ink-soft: #6d7077;
    --grey-light: #efefef;
    --grey-mid: #d7d6d8;
    --grey-deep: #c4c2c4;
    --page: #ffffff;
  }
  * { box-sizing: border-box; margin: 0; padding: 0; }
  html, body { width: 947px; height: 1200px; overflow: hidden; background: var(--page); }
  .sheet { position: relative; width: 947px; height: 1200px; }
  .card {
    position: absolute; left: 13px; width: 921px; height: 567px; overflow: hidden;
    font-family: "Didact Gothic", sans-serif; font-weight: 400; color: var(--ink);
  }
  .card--front { top: 13px; background: radial-gradient(ellipse at 50% 85%, var(--grey-light) 0%, var(--grey-mid) 60%, var(--grey-deep) 100%); }
  .card--back { top: 604px; background: linear-gradient(125deg, var(--grey-mid) 0%, var(--grey-light) 40%, var(--grey-mid) 65%, var(--grey-deep) 100%); }
  .texture { position: absolute; inset: 0; }
  .brand {
    position: absolute; display: flex; align-items: center; gap: 14px;
    font-family: "Didact Gothic", sans-serif; font-weight: 400; color: var(--crimson); white-space: nowrap;
  }
  .brand__dot { border-radius: 50%; background: var(--crimson); flex: none; }
  .card--front .brand { left: 0; right: 0; justify-content: center; top: 240px; font-size: 60px; letter-spacing: 1px; }
  .card--front .brand__dot { width: 44px; height: 44px; }
  .website { position: absolute; left: 0; right: 0; top: 372px; text-align: center; font-size: 24px; letter-spacing: 2px; color: var(--ink); }
  .band { position: absolute; left: 0; bottom: 0; width: 921px; height: 130px; }
  .contact-name { position: absolute; left: 0; width: 617px; top: 166px; text-align: center; font-size: 28px; font-weight: 400; letter-spacing: 1px; }
  .contact-role { position: absolute; left: 0; width: 617px; top: 204px; text-align: center; font-size: 24px; font-variant: small-caps; letter-spacing: 1.5px; color: var(--ink-soft); }
  .rule { position: absolute; left: 84px; top: 257px; width: 428px; height: 2px; background: var(--crimson); }
  .details { position: absolute; left: 0; width: 640px; top: 340px; text-align: center; line-height: 33px; }
  .details__email { font-family: "Open Sans", sans-serif; font-size: 22px; color: var(--ink); }
  .details__line { font-size: 24px; color: var(--ink-soft); letter-spacing: 1px; }
  .details__label { font-variant: small-caps; font-size: 22px; }
  .dots { position: absolute; left: 569px; top: 60px; width: 12px; height: 466px; }
  .card--back .brand { left: 604px; top: 482px; font-size: 31px; gap: 8px; }
  .card--back .brand__dot { width: 22px; height: 22px; }
</style>
</head>
<body>
<main class="sheet">
  <section class="card card--front" aria-label="Card front">
    <div class="texture" role="img" aria-label="Faint grey architectural background texture"></div>
    <div class="brand"><span class="brand__dot"></span><span class="brand__name">VALTRION TOOLS</span></div>
    <p class="website">WWW.VALTRION.COM.SG</p>
    <svg class="band" viewBox="0 0 921 130" preserveAspectRatio="none" aria-hidden="true">
      <path d="M0 55 Q480 -5 921 130 Q520 80 240 130 L0 130 Z" fill="var(--crimson)"/>
    </svg>
  </section>

  <section class="card card--back" aria-label="Card back">
    <div class="texture" role="img" aria-label="Faint grey architectural background texture"></div>
    <h1 class="contact-name">DANIEL KOH</h1>
    <p class="contact-role">Project Manager</p>
    <div class="rule"></div>
    <div class="details">
      <p class="details__email">d.koh@valtrion.com.sg</p>
      <p class="details__line"><span class="details__label">office:</span> +65.6000.62.00</p>
      <p class="details__line"><span class="details__label">fax:</span> +65.6000.00.00</p>
    </div>
    <svg class="dots" viewBox="0 0 12 466" aria-hidden="true">
      <line x1="6" y1="6" x2="6" y2="460" stroke="var(--crimson)" stroke-width="10" stroke-linecap="round" stroke-dasharray="0 15.6"/>
    </svg>
    <div class="brand"><span class="brand__dot"></span><span class="brand__name">VALTRION TOOLS</span></div>
  </section>
</main>
</body>
</html>
```